Marlo Tidy Yard Website

We need a website design for this new company. I've attached the company logo. This company is in the construction industry that provides general labor, maintenance and cleaning for construction sites. We want a clean and simple website that can be easy to navigate.

Target Market(s)

Construction industry

Industry/Entity Type

Construction

Number of Pages Required

2 page

Font styles to use
Sans Serif

```html
<!DOCTYPE html>
<html lang="en">
<head>
<meta charset="utf-8">
<title>Marlo Tidy Yard</title>
<link href="https://fonts.googleapis.com/css2?family=Poppins:wght@400;500;600;700;800&display=swap" rel="stylesheet">
<style>
:root{
  --navy:#0b0a63;
  --orange:#f26b0f;
  --text:#333;
  --muted:#555;
  --light:#f6f6f6;
  --line:#dcdcdc;
  --footer:#3f3f3f;
  --footer-bar:#2f2f2f;
  --white:#fff;
}
*{box-sizing:border-box;margin:0;padding:0}
html,body{width:1200px;height:2579px;overflow:hidden}
body{font-family:"Poppins",sans-serif;color:var(--text);background:var(--white);position:relative}
.accent{color:var(--orange)}
.pill{position:absolute;display:flex;align-items:center;justify-content:center;border-radius:30px;font-weight:500;color:var(--white);background:var(--navy)}

/* header */
.site-header{position:absolute;left:0;top:0;width:1200px;height:93px;background:var(--white)}
.brand{position:absolute;left:143px;top:28px;display:flex;align-items:center;gap:10px;font-weight:800;font-size:27px;color:var(--navy);letter-spacing:-.3px}
.brand-square{width:32px;height:32px;background:var(--orange)}
.header-contact{position:absolute;top:22px;display:flex;gap:10px;align-items:center;white-space:nowrap}
.header-contact small{display:block;font-size:11.5px;color:var(--orange)}
.header-contact span{display:block;font-size:14px;color:var(--text)}
.socials{position:absolute;display:flex;gap:5px}
.socials i{display:block;width:25px;height:25px;border-radius:50%;background:var(--navy)}

/* hero */
.hero{position:absolute;left:0;top:93px;width:1200px;height:507px;overflow:hidden}
.hero-photo{position:absolute;inset:0;background:linear-gradient(180deg,#3e6d9e 0%,#8aa7c4 30%,#b08a58 55%,#c6c23a 80%,#8b6a3c 100%)}
.hero-shade{position:absolute;inset:0;background:linear-gradient(180deg,rgba(0,0,0,.15),rgba(0,0,0,.25))}
.hero h1{position:absolute;left:0;width:1200px;top:55px;text-align:center;color:var(--white);font-weight:500;font-size:40px;line-height:54px}
.hero .pill{left:466px;top:193px;width:237px;height:45px;font-size:16px;letter-spacing:.4px}
.hero-wave{position:absolute;left:0;bottom:0}

/* about */
.section-title{font-size:33px;font-weight:600;color:var(--navy)}
.about-title{position:absolute;left:143px;top:655px}
.title-rule{position:absolute;height:2px;background:linear-gradient(90deg,var(--line),var(--line) 60%,transparent)}
.about-copy{position:absolute;left:143px;top:740px;width:570px}
.about-lead{font-size:12px;font-weight:600;line-height:21px;color:#222}
.about-body{margin-top:4px;font-size:12px;line-height:21.5px;color:var(--muted)}
.about-copy .pill{position:static;margin-top:12px;width:153px;height:36px;font-size:14px;margin-left:-2px}
.about-photo{position:absolute;left:742px;top:672px;width:316px;height:316px;border-radius:50%;background:radial-gradient(circle at 40% 40%,#e9e6df,#9aa0a6 55%,#e07d2a 100%)}

/* services */
.services{position:absolute;left:0;top:1050px;width:1200px;height:680px;background:var(--light)}
.services-title{position:absolute;left:0;width:1200px;top:45px;text-align:center}
.card{position:absolute;top:148px;width:291px;height:369px;background:var(--white);border-radius:4px;box-shadow:0 1px 4px rgba(0,0,0,.08)}
.card-photo{position:absolute;left:0;top:0;width:291px;height:174px;border-radius:4px 4px 0 0}
.card-icon{position:absolute;left:108px;top:136px;width:76px;height:76px;border-radius:50%}
.card h3{position:absolute;left:0;width:291px;top:222px;text-align:center;font-size:15px;font-weight:600}
.card p{position:absolute;left:12px;width:267px;top:250px;text-align:center;font-size:12.5px;line-height:20.5px;color:var(--muted)}
.card-plus{position:absolute;left:130px;top:354px;width:30px;height:30px;border-radius:50%}
.services .pill{left:524px;top:560px;width:153px;height:37px;font-size:14px}

/* quick contact */
.quick{position:absolute;left:0;top:1730px;width:1200px;height:518px;background:linear-gradient(180deg,#fffdf6 0%,#fff6dc 55%,#fde7a8 100%)}
.quick-title{position:absolute;left:0;width:1200px;top:60px;text-align:center}
.quick-intro{position:absolute;left:270px;width:660px;top:135px;text-align:center;font-size:12.5px;line-height:24px;color:var(--text)}
.field{position:absolute;height:42px;background:var(--white);border:1px solid #d9d9d9;border-radius:3px;display:flex;align-items:center;font-size:11.5px;color:#555}
.field .ico{width:36px;height:100%;display:flex;align-items:center;justify-content:center;border-right:1px solid #e3e3e3;margin-right:10px}
.field.message{align-items:flex-start;height:85px}
.field.message .ico{height:28px;border-right:1px solid #e3e3e3}
.field.message span{margin-top:8px}
.submit{position:absolute;left:532px;top:410px;width:137px;height:38px;border-radius:20px;background:var(--orange);color:var(--white);font-size:13px;font-weight:600;letter-spacing:.8px;display:flex;align-items:center;justify-content:center}

/* footer */
.site-footer{position:absolute;left:0;top:2248px;width:1200px;height:282px;background:var(--footer);color:var(--white)}
.footer-head{position:absolute;top:52px;font-size:15px;font-weight:500}
.footer-rule{position:absolute;top:80px;height:2px;width:120px;background:linear-gradient(90deg,#888,transparent)}
.contact-item{position:absolute;left:143px;display:flex;align-items:flex-start;gap:14px;font-size:12.5px;line-height:19px}
.contact-item .dot{width:26px;height:26px;border-radius:50%;background:var(--navy);flex:none;display:flex;align-items:center;justify-content:center}
.map{position:absolute;left:464px;top:99px;width:330px;height:141px;border:2px solid #999;background:linear-gradient(135deg,#e8e4da,#d9dccf 60%,#f2d77a)}
.footer-brand{position:absolute;left:906px;top:140px;font-weight:800;font-size:22px;line-height:28px;color:var(--white);display:flex;align-items:center;gap:8px}
.footer-brand i{display:block;width:22px;height:22px;background:var(--orange)}
.footer-bar{position:absolute;left:0;top:2530px;width:1200px;height:49px;background:var(--footer-bar);color:#ddd;font-size:12px;display:flex;align-items:center;justify-content:center}
</style>
</head>
<body>

<header class="site-header">
  <div class="brand"><span class="brand-square"></span>Marlo Tidy Yard</div>
  <div class="header-contact" style="left:545px">
    <svg width="30" height="30" viewBox="0 0 24 24" fill="none" stroke="#222" stroke-width="1.5"><path d="M5 3h4l2 5-2.5 1.5a11 11 0 0 0 6 6L16 13l5 2v4a2 2 0 0 1-2 2A16 16 0 0 1 3 5a2 2 0 0 1 2-2z"/></svg>
    <div><small>Request call back</small><span>(555) 014-2290</span></div>
  </div>
  <div class="header-contact" style="left:712px">
    <svg width="28" height="28" viewBox="0 0 24 24" fill="none" stroke="#222" stroke-width="1.5"><rect x="3" y="5" width="18" height="14"/><path d="M3 5l9 8 9-8"/></svg>
    <div><small>Write us</small><span>info@marlotidyyard.com</span></div>
  </div>
  <div class="socials" style="left:947px;top:31px"><i></i><i></i><i></i><i></i></div>
</header>

<section class="hero">
  <div class="hero-photo" role="img" aria-label="Photo of construction workers in hard hats and safety vests looking up at a building site"></div>
  <div class="hero-shade"></div>
  <h1>Helping You And Your House Become<br>Better Acquainted.</h1>
  <div class="pill">CONTACT US TODAY</div>
  <svg class="hero-wave" width="1200" height="80" viewBox="0 0 1200 80"><path d="M0 60 C200 20 400 10 600 45 C800 80 1000 70 1200 20 L1200 80 L0 80 Z" fill="#fff"/></svg>
</section>

<section class="about">
  <h2 class="section-title about-title">About Marlo <span class="accent">Tidy Yard</span></h2>
  <div class="title-rule" style="left:143px;top:713px;width:250px"></div>
  <div class="about-copy">
    <p class="about-lead">Lorem ipsum dolor sit amet, consectetuer adipiscing elit, sed diam nonmmy nih euismod tincunt ut laoreet dolore magna aliquam erat volutpat Ut wisi enim ad minim veniam.</p>
    <p class="about-body">Lorem ipsum dolor sit amet, consectetuer adipiscing elit, sed diam nonummy nibh euismod tincidunt ut laoreet dolore magna aliquam erat volutpat. Ut wisi enim ad minim veniam, quis nostrud exerci tation ullamcorper suscipit lobortis nisl ut aliquip ex ea commodo consequat. Duis autem vel eum iriure dolot laoreet dolore magna aliquam erat volutpat. Ut wisi enim ad minim veniam, quis nostrud exerci tation ullamcorper suscipit lobortis nisl ut aliquip ex ea commodo consequat. Duis autem vel eum iriure dolor in hendrerit in vulputate velit esse molestie consequat, vel illum dolore eu feugiat nulla facilr.</p>
    <div class="pill">Contact Us Today</div>
  </div>
  <div class="about-photo" role="img" aria-label="Photo of site workers in hard hats reviewing building plans"></div>
</section>

<section class="services">
  <h2 class="section-title services-title">Our <span class="accent">Services</span></h2>
  <div class="title-rule" style="left:540px;top:96px;width:140px;background:linear-gradient(90deg,transparent,var(--line),transparent)"></div>

  <article class="card" style="left:142px">
    <div class="card-photo" role="img" aria-label="Photo of general labor crew working on a site deck" style="background:linear-gradient(180deg,#dfe3e6,#9a8d70 70%,#6f5f45)"></div>
    <div class="card-icon" style="background:var(--navy)"></div>
    <h3 style="color:var(--navy)">General Labor</h3>
    <p>Lorem ipsum dolor sit consectetudipiscing sed diam nonmmy nibh euismod tincunt ut laoareet dolore meagna consectetuer adipiscing&nbsp; sed diam nonmmy.</p>
    <div class="card-plus" style="background:var(--navy)"><svg width="30" height="30" viewBox="0 0 30 30" stroke="#fff" stroke-width="2"><path d="M15 9v12M9 15h12"/></svg></div>
  </article>

  <article class="card" style="left:455px">
    <div class="card-photo" role="img" aria-label="Photo of workers shovelling material for maintenance work" style="background:linear-gradient(180deg,#2c6bc7,#7fb0e6 50%,#d9d6cf)"></div>
    <div class="card-icon" style="background:var(--orange)"></div>
    <h3 style="color:var(--orange)">Maintenance&nbsp; Works</h3>
    <p>Lorem ipsum dolor sit consectetudipiscing sed diam nonmmy nibh euismod tincunt ut laoareet dolore meagna consectetuer adipiscing&nbsp; sed diam nonmmy.</p>
    <div class="card-plus" style="background:var(--orange)"><svg width="30" height="30" viewBox="0 0 30 30" stroke="#fff" stroke-width="2"><path d="M15 9v12M9 15h12"/></svg></div>
  </article>

  <article class="card" style="left:768px">
    <div class="card-photo" role="img" aria-label="Photo of a worker sweeping a concrete floor on a construction site" style="background:linear-gradient(180deg,#cfcfcb,#b9b8b2 60%,#8d9a7a)"></div>
    <div class="card-icon" style="background:var(--orange)"></div>
    <h3 style="color:var(--orange)">Cleaning For Construction Sites</h3>
    <p>Lorem ipsum dolor sit consectetudipiscing sed diam nonmmy nibh euismod tincunt ut laoareet dolore meagna consectetuer adipiscing&nbsp; sed diam nonmmy.</p>
    <div class="card-plus" style="background:var(--orange)"><svg width="30" height="30" viewBox="0 0 30 30" stroke="#fff" stroke-width="2"><path d="M15 9v12M9 15h12"/></svg></div>
  </article>

  <div class="pill">Contact Us Today</div>
</section>

<section class="quick">
  <h2 class="section-title quick-title">Quick <span class="accent">Contact</span></h2>
  <div class="title-rule" style="left:540px;top:112px;width:140px;background:linear-gradient(90deg,transparent,var(--line),transparent)"></div>
  <p class="quick-intro">Lorem ipsum dolor sit amet, consectetuer adipiscing elit, sed diam nonmmy nibh euismod tincunt ut laoreet dolore magna aliquam erat volutpat Ut wisi enim ad minim veniam.</p>

  <div class="field" style="left:303px;top:200px;width:289px"><span class="ico"><svg width="12" height="12" viewBox="0 0 12 12" fill="var(--navy)"><circle cx="6" cy="3.5" r="2.8"/><path d="M0.5 12a5.5 4.5 0 0 1 11 0z"/></svg></span><span>First Name*</span></div>
  <div class="field" style="left:608px;top:200px;width:289px"><span class="ico"><svg width="12" height="12" viewBox="0 0 12 12" fill="var(--navy)"><circle cx="6" cy="3.5" r="2.8"/><path d="M0.5 12a5.5 4.5 0 0 1 11 0z"/></svg></span><span>Last Name*</span></div>
  <div class="field" style="left:303px;top:255px;width:289px"><span class="ico"><svg width="12" height="12" viewBox="0 0 24 24" fill="var(--navy)"><path d="M5 2h4l2 5-2.5 1.5a11 11 0 0 0 6 6L16 12l5 2v4a2 2 0 0 1-2 2A17 17 0 0 1 3 4a2 2 0 0 1 2-2z"/></svg></span><span>Your Phone*</span></div>
  <div class="field" style="left:608px;top:255px;width:289px"><span class="ico"><svg width="13" height="10" viewBox="0 0 13 10" fill="var(--navy)"><path d="M0 0h13v1.5L6.5 5.5 0 1.5zM0 3l6.5 4L13 3v7H0z"/></svg></span><span>Your Email*</span></div>
  <div class="field message" style="left:303px;top:310px;width:594px"><span class="ico"><svg width="13" height="11" viewBox="0 0 13 11" fill="var(--navy)"><ellipse cx="6" cy="4" rx="6" ry="4"/><path d="M2 6l-1 4 4-2.5z"/></svg></span><span>Your Message*</span></div>
  <div class="submit">SUBMIT NOW</div>
</section>

<footer class="site-footer">
  <div class="footer-head" style="left:143px">Contact Details</div>
  <div class="footer-rule" style="left:143px"></div>
  <div class="contact-item" style="top:102px"><span class="dot"><svg width="10" height="13" viewBox="0 0 10 13" fill="#fff"><path d="M5 0a5 5 0 0 1 5 5c0 3-5 8-5 8S0 8 0 5a5 5 0 0 1 5-5z"/><circle cx="5" cy="5" r="1.8" fill="var(--navy)"/></svg></span><span>Street Name City Name<br>State Zipcode</span></div>
  <div class="contact-item" style="top:145px"><span class="dot"><svg width="12" height="12" viewBox="0 0 24 24" fill="#fff"><path d="M5 2h4l2 5-2.5 1.5a11 11 0 0 0 6 6L16 12l5 2v4a2 2 0 0 1-2 2A17 17 0 0 1 3 4a2 2 0 0 1 2-2z"/></svg></span><span style="margin-top:3px">(555) 014-2290</span></div>
  <div class="contact-item" style="top:181px"><span class="dot"><svg width="12" height="12" viewBox="0 0 12 12" fill="#fff"><rect x="3" y="0" width="6" height="3"/><rect x="0" y="4" width="12" height="5" rx="1"/><rect x="3" y="7" width="6" height="5"/></svg></span><span style="margin-top:3px">(555) 014-2291</span></div>
  <div class="contact-item" style="top:219px"><span class="dot"><svg width="12" height="10" viewBox="0 0 13 10" fill="#fff"><path d="M0 0h13v1.5L6.5 5.5 0 1.5zM0 3l6.5 4L13 3v7H0z"/></svg></span><span style="margin-top:3px">info@marlotidyyard.com</span></div>

  <div class="footer-head" style="left:464px;top:45px">Location Map</div>
  <div class="footer-rule" style="left:464px;top:73px"></div>
  <div class="map" role="img" aria-label="Street map showing the company location with a marker pin"></div>

  <div class="footer-head" style="left:906px">Follow Us</div>
  <div class="footer-rule" style="left:906px;width:70px"></div>
  <div class="socials" style="left:906px;top:98px"><i></i><i></i><i></i><i></i></div>
  <div class="footer-brand"><i></i>Marlo Tidy Yard</div>
</footer>
<div class="footer-bar">Copyright © 2019 Marlo Tidy Yard. All Rights Reserved.</div>

</body>
</html>
```